Quillstone Huddle Post Card for Personal Promotion

This is a new application soon to be released on the market in the US.

A web site is underdevelopment but the current link is:
http://www.quillstonehuddle.example/index_BACKUP.html

This application is intended to help a project manager or administrator schedule, deliver and communication activities for a group meeting. The application is organized around the following areas:

Scheduled Meetings
Meetings Underway
Completed Meetings
Canceled Meetings

Scheduling Phase
* Multiple facilitator-defined roles to organize meeting activities and communication
* Meeting Objective
* Pre-Meeting Instructions
* Pre-Meeting Attachments including the agenda in PDF format
* Multiple Administrators (requires QuillstoneHuddle license for each administrator)
* Conference/Teleconference Contact Information
* System generated comments for speakers outlining date, time and location
* Agenda Management with Breakout Session Support
* Sends email meeting invites with calendar invite, agenda and attachments

Meeting Underway Phase
* Displays current time, remaining meeting time and remaining session time to help keep meetings on schedule
* Attendance Tracking to mark when a participant arrives
* Activity Log provides quick access to meeting activities
* Up to date meeting minutes created on demand
* Session specific attachments
* Documentation of meeting action items, decisions, notes, potential risks and known issues

Completed Phase
* Role specific post meeting communications
* Optional inclusion of original agenda in PDF format
* Optional inclusion of all attachments including session attachments (up to 20 per meeting)
* Optional inclusion of user specific action items
* Follow up reminders (user defined days before due date) for participants that have action items

Canceled
* Send customized message to participants

Target Market(s)

Business people who schedule and lead meetings.

Font styles to use
Serif

Colors
faa54b
33b8a4

Requirements
Must have
• call to action: go to web site (www.quillstonehuddle.example)
• Include color scheme from logo

```html
<!DOCTYPE html>
<html lang="en">
<head>
<meta charset="utf-8">
<title>Quillstone Huddle Postcard</title>
<link href="https://fonts.googleapis.com/css2?family=Open+Sans:wght@300;400;600;700;800&display=swap" rel="stylesheet">
<style>
:root{
  --navy:#0c1a2e;
  --navy-deep:#07111f;
  --navy-mid:#16304d;
  --teal:#33b8a4;
  --teal-light:#8fe7e0;
  --teal-dark:#2a8f8a;
  --orange:#f26f4f;
  --orange-light:#faa54b;
  --ink:#0d1b30;
  --white:#ffffff;
  --page:#ecebe8;
  --line:#333333;
}
*{box-sizing:border-box;margin:0;padding:0}
html,body{width:850px;height:1200px;overflow:hidden}
body{background:var(--page);font-family:"Open Sans",Arial,sans-serif;position:relative}

.card{position:absolute;left:70px;width:710px;height:546px;overflow:hidden;box-shadow:0 4px 14px rgba(0,0,0,.25)}
.card-front{top:32px;background:linear-gradient(135deg,var(--navy-mid) 0%,var(--navy) 45%,var(--navy-deep) 100%)}
.card-back{top:622px;background:var(--white)}

/* front */
.intro{position:absolute;left:19px;top:80px;width:320px;color:var(--white);font-size:17.5px;line-height:24.5px}
.areas{position:absolute;left:19px;top:248px;list-style:none}
.areas li{display:flex;align-items:center;height:45px;color:var(--white);font-size:18px}
.areas svg{width:36px;height:40px;margin-right:13px}

.brand{position:absolute;color:var(--teal);font-weight:400;white-space:nowrap;display:flex;align-items:center}
.brand .dot{border-radius:50%;background:var(--orange);display:inline-block}
.brand-front{right:28px;top:30px;font-size:29px;letter-spacing:1px;gap:8px}
.brand-front .dot{width:14px;height:14px}
.tagline{position:absolute;right:27px;top:90px;text-align:right;color:var(--white)}
.tagline .kicker{color:var(--orange);font-weight:300;font-size:21px;letter-spacing:.5px;line-height:28px}
.tagline .headline{font-weight:800;font-size:23px;letter-spacing:.6px;line-height:32px}
.tagline .sub{font-weight:700;font-size:12.6px;line-height:22px}

.screen{position:absolute;left:352px;top:196px;width:334px;height:229px;border-radius:16px;border:3px solid #d9dde0;
  background:linear-gradient(180deg,#3a9e8c 0%,#4c8a84 40%,#6f7476 100%)}

.footer-band{position:absolute;left:0;top:438px;width:710px;height:108px}
.contact{position:absolute;left:20px;top:457px;display:flex;gap:8px;color:var(--ink);font-weight:700;font-size:17px;line-height:24px}
.contact svg{width:18px;height:22px;margin-top:2px}
.cta{position:absolute;right:22px;top:447px;text-align:right;color:var(--ink);font-weight:800}
.cta .call{font-size:25px;line-height:30px}
.cta .phone{font-size:25px;line-height:30px}
.cta .url{font-size:16px;font-weight:700;display:flex;align-items:center;gap:6px;justify-content:flex-end;margin-top:2px}

/* back */
.back-art{position:absolute;left:0;top:0;width:710px;height:546px}
.pill{position:absolute;left:0;height:34px;border-radius:0 17px 17px 0;background:linear-gradient(90deg,var(--teal-dark),var(--teal-light));
  color:var(--ink);font-weight:700;font-size:17px;line-height:34px;padding-left:19px}
.pill-cost{top:33px;width:181px}
.pill-included{top:161px;width:215px}
.back-copy{position:absolute;left:18px;color:var(--white);font-size:15.5px;line-height:22px}
.copy-cost{top:82px;width:260px}
.copy-included{top:206px;width:290px}
.url-pill{position:absolute;left:20px;top:419px;width:287px;height:27px;border-radius:14px;background:linear-gradient(90deg,var(--teal-dark),var(--teal-light));
  color:var(--ink);font-weight:700;font-size:15px;line-height:27px;text-align:center}
.brand-back{left:380px;top:44px;font-size:16px;letter-spacing:.5px;gap:6px}
.brand-back .dot{width:9px;height:9px}
.stamp{position:absolute;left:590px;top:26px;width:96px;height:96px;border:1.5px solid var(--line)}
.address-line{position:absolute;left:438px;width:247px;border-top:1.5px solid var(--line)}
</style>
</head>
<body>

<section class="card card-front">
  <p class="intro">This application is intended to help a project manager or administrator schedule, deliver and communication activities for a group meeting. The application is organized around the following areas</p>

  <ul class="areas">
    <li><svg viewBox="0 0 36 40"><polygon points="18,1 34,10 34,30 18,39 2,30 2,10" fill="var(--orange)" stroke="var(--orange-light)" stroke-width="1.5"/><rect x="11" y="13" width="14" height="13" fill="none" stroke="#fff" stroke-width="1.6"/><line x1="11" y1="17" x2="25" y2="17" stroke="#fff" stroke-width="1.6"/></svg>Scheduled Meetings</li>
    <li><svg viewBox="0 0 36 40"><polygon points="18,1 34,10 34,30 18,39 2,30 2,10" fill="var(--orange)" stroke="var(--orange-light)" stroke-width="1.5"/><circle cx="18" cy="14" r="3" fill="#fff"/><circle cx="11" cy="17" r="2.4" fill="#fff"/><circle cx="25" cy="17" r="2.4" fill="#fff"/><rect x="14" y="18" width="8" height="8" rx="2" fill="#fff"/><rect x="8" y="20" width="6" height="6" rx="2" fill="#fff"/><rect x="22" y="20" width="6" height="6" rx="2" fill="#fff"/></svg>Meetings Underway</li>
    <li><svg viewBox="0 0 36 40"><polygon points="18,1 34,10 34,30 18,39 2,30 2,10" fill="var(--orange)" stroke="var(--orange-light)" stroke-width="1.5"/><rect x="11" y="11" width="13" height="17" fill="none" stroke="#fff" stroke-width="1.6"/><line x1="14" y1="16" x2="21" y2="16" stroke="#fff" stroke-width="1.4"/><line x1="14" y1="20" x2="21" y2="20" stroke="#fff" stroke-width="1.4"/><polyline points="19,26 22,29 27,23" fill="none" stroke="#fff" stroke-width="1.8"/></svg>Completed Meetings</li>
    <li><svg viewBox="0 0 36 40"><polygon points="18,1 34,10 34,30 18,39 2,30 2,10" fill="var(--orange)" stroke="var(--orange-light)" stroke-width="1.5"/><rect x="10" y="12" width="16" height="15" fill="none" stroke="#fff" stroke-width="1.6"/><line x1="10" y1="17" x2="26" y2="17" stroke="#fff" stroke-width="1.4"/><line x1="10" y1="22" x2="26" y2="22" stroke="#fff" stroke-width="1.2"/><line x1="15" y1="17" x2="15" y2="27" stroke="#fff" stroke-width="1.2"/><line x1="21" y1="17" x2="21" y2="27" stroke="#fff" stroke-width="1.2"/></svg>Canceled Meetings</li>
  </ul>

  <div class="brand brand-front">QUILLSTONE HUDDLE <span class="dot"></span></div>

  <div class="tagline">
    <div class="kicker">MEETING MANAGEMENT</div>
    <div class="headline">A PRODUCTIVITY TOOL FOR</div>
    <div class="sub">PROJECT MANAGERS AND MEETING FACILITATORS</div>
  </div>

  <div class="screen" role="img" aria-label="Tablet showing the meeting dashboard of the application"></div>

  <svg class="footer-band" viewBox="0 0 710 108" preserveAspectRatio="none">
    <defs>
      <linearGradient id="tealBand" x1="0" x2="1"><stop offset="0" stop-color="#2f9f9a"/><stop offset=".7" stop-color="#8fe7e0"/><stop offset="1" stop-color="#a5f0ea"/></linearGradient>
      <linearGradient id="orangeBand" x1="0" x2="1"><stop offset="0" stop-color="#f9a27f"/><stop offset="1" stop-color="#f26f4f"/></linearGradient>
    </defs>
    <polygon points="0,0 375,0 405,108 0,108" fill="url(#tealBand)"/>
    <polygon points="375,0 710,0 710,108 405,108" fill="#fff"/>
    <polygon points="383,0 710,0 710,108 414,108" fill="url(#orangeBand)"/>
  </svg>

  <div class="contact">
    <svg viewBox="0 0 18 22"><path d="M9 1a7 7 0 0 0-7 7c0 5 7 13 7 13s7-8 7-13a7 7 0 0 0-7-7z" fill="none" stroke="var(--ink)" stroke-width="2"/><circle cx="9" cy="8" r="2.5" fill="var(--ink)"/></svg>
    <div>Quillstone Works, Inc.<br>PO Box 4182 Larchmont,<br>Vermont 05099</div>
  </div>

  <div class="cta">
    <div class="call">Call US</div>
    <div class="phone">555-014-2387</div>
    <div class="url">www.quillstonehuddle.example
      <svg width="20" height="20" viewBox="0 0 20 20"><circle cx="10" cy="10" r="9" fill="none" stroke="var(--ink)" stroke-width="1.6"/><ellipse cx="10" cy="10" rx="4" ry="9" fill="none" stroke="var(--ink)" stroke-width="1.3"/><line x1="1" y1="10" x2="19" y2="10" stroke="var(--ink)" stroke-width="1.3"/></svg>
    </div>
  </div>
</section>

<section class="card card-back">
  <svg class="back-art" viewBox="0 0 710 546">
    <defs>
      <linearGradient id="backDark" x1="0" y1="0" x2="1" y2="1"><stop offset="0" stop-color="#1b3452"/><stop offset=".6" stop-color="#0c1a2e"/><stop offset="1" stop-color="#07111f"/></linearGradient>
      <linearGradient id="arcOrange" x1="0" y1="0" x2="0" y2="1"><stop offset="0" stop-color="#f26f4f"/><stop offset=".5" stop-color="#f9a27f"/><stop offset="1" stop-color="#f26f4f"/></linearGradient>
    </defs>
    <path d="M300,0 L318,0 Q470,220 332,454 L327,454 Q440,220 300,0Z" fill="var(--teal)"/>
    <path d="M252,0 L310,0 Q455,220 330,454 L320,454 Q420,220 252,0Z" fill="url(#arcOrange)"/>
    <path d="M0,0 L250,0 Q415,220 318,454 L0,454Z" fill="url(#backDark)" role="img" aria-label="Dimmed meeting room backdrop"/>
  </svg>

  <div class="pill pill-cost">WHAT IS COST</div>
  <p class="back-copy copy-cost">The current introductory price is reduced from $179 to $150 until January 1st, 2018.</p>

  <div class="pill pill-included">WHAT IS INCLUDED</div>
  <p class="back-copy copy-included">Unlimited meetings during the subscription period. Total number of participants per meeting is currently one-hundred (100). Up to 20 email attachments are possible for meeting invites and minutes--not including the agenda or meeting minutes. Contact us if you need more than 100 people or additional attachments to emails.</p>

  <div class="url-pill">www.quillstonehuddle.example</div>

  <div class="brand brand-back">QUILLSTONE HUDDLE <span class="dot"></span></div>
  <div class="stamp"></div>
  <div class="address-line" style="top:301px"></div>
  <div class="address-line" style="top:345px"></div>
  <div class="address-line" style="top:388px"></div>
</section>

</body>
</html>
```